Flyer Re-Design

We need a flyer re-design for a company that recently started doing it's own graphic design. Although we've taken a first attempt at the design, we would like a design professional, like yourself show us how much better you can do it. We're going through a re-branding as the logo reads "formerly" known as and although we'd like to keep the logo as it is---everything else should be more contemporary.

5.5" x 8.5" or 5" x 7"

Target Market(s)

Bahamas Youth

Industry/Entity Type

Graphic Design

Font styles to use
Sans Serif

Requirements
Must have
• Current Logo. Include as many details as already listed in the document.
Nice to have
• Fresh New, Crisp Ideas for this Pharmacy rebranding
Should not have
• Too Many colors or serif fonts

```html
<!DOCTYPE html>
<html lang="en">
<head>
<meta charset="utf-8">
<title>Vital Leaf Pharmacy – Rewards Club Flyer</title>
<link href="https://fonts.googleapis.com/css2?family=Roboto:wght@400;500;700&display=swap" rel="stylesheet">
<style>
  :root {
    --backdrop: #8c8c8c;
    --paper: #ffffff;
    --brand-green: #3a7d3a;
    --brand-red: #c0392b;
    --ink: #1a1a1a;
    --photo-light: #eef1ef;
    --photo-mid: #cfd8d2;
  }
  * { box-sizing: border-box; margin: 0; padding: 0; }
  html, body { width: 1200px; height: 900px; overflow: hidden; }
  body {
    background: var(--backdrop);
    font-family: "Roboto", Arial, sans-serif;
    color: var(--ink);
    position: relative;
  }
  .flyer {
    position: absolute;
    left: 320px; top: 17px;
    width: 560px; height: 866px;
    background: var(--paper);
    overflow: hidden;
  }
  .brand {
    position: absolute; left: 28px; top: 30px;
  }
  .brand-name {
    font-size: 25px; font-weight: 500; color: var(--brand-green);
    letter-spacing: 0.3px;
  }
  .brand-former {
    font-size: 12px; font-weight: 500; color: var(--ink);
    text-transform: uppercase; letter-spacing: 1px; margin-top: 4px;
  }
  .hero-photo {
    position: absolute; left: 0; top: 100px;
    width: 560px; height: 370px;
    background: linear-gradient(100deg, var(--photo-mid) 0%, var(--photo-light) 45%, #f7f8f7 70%, var(--photo-mid) 100%);
  }
  .rewards-panel {
    position: absolute; left: 0; top: 128px;
    width: 318px; height: 230px;
    background: var(--brand-green);
    clip-path: polygon(0 0, 88% 0, 100% 22%, 100% 100%, 0 100%);
    color: #fff;
    padding: 18px 20px 0 24px;
  }
  .rewards-title {
    font-size: 28px; font-weight: 500; line-height: 1.08;
    text-transform: uppercase; text-align: center; margin-bottom: 12px;
  }
  .rewards-list { list-style: none; }
  .rewards-list li {
    font-size: 13.5px; line-height: 1.1; margin-bottom: 6px;
    display: flex; gap: 6px;
  }
  .rewards-list svg { flex: 0 0 12px; margin-top: 1px; }
  .thanks-band {
    position: absolute; left: 0; top: 470px;
    width: 560px; height: 40px;
    background: var(--brand-green); color: #fff;
    font-size: 20px; text-align: center; line-height: 40px;
  }
  .thanks-band strong { font-weight: 700; text-transform: uppercase; }
  .service-pennant {
    position: absolute; left: 28px; top: 510px;
    width: 205px; height: 200px;
  }
  .service-pennant svg { position: absolute; inset: 0; }
  .service-text {
    position: absolute; left: 0; top: 22px; width: 205px;
    text-align: center; color: #fff;
    font-size: 17px; font-weight: 500; line-height: 1.4;
    text-transform: uppercase;
  }
  .exclusives {
    position: absolute; left: 262px; top: 520px; width: 290px;
  }
  .exclusives-title {
    font-size: 25px; font-weight: 500; text-transform: uppercase;
    letter-spacing: 1px; margin-bottom: 8px;
  }
  .exclusives-list { list-style: none; }
  .exclusives-list li {
    font-size: 13.5px; line-height: 1.5;
  }
  .exclusives-list li::before { content: "• "; }
  .contact {
    position: absolute; left: 0; top: 740px; width: 560px;
    text-align: center; font-size: 14px; font-weight: 500; line-height: 1.45;
  }
</style>
</head>
<body>
  <main class="flyer">
    <header class="brand">
      <div class="brand-name">VITAL LEAF PHARMACY</div>
      <div class="brand-former">Formerly K.T.N. Drugs Co. Ltd.</div>
    </header>

    <div class="hero-photo" role="img" aria-label="Smiling pharmacist in a white coat holding a clipboard in front of pharmacy shelves"></div>

    <section class="rewards-panel">
      <h1 class="rewards-title">Join Our<br>Rewards Club</h1>
      <ul class="rewards-list">
        <li><svg width="12" height="12" viewBox="0 0 12 12"><path d="M1 6.5l3 3 7-7" fill="none" stroke="#fff" stroke-width="1.8"/></svg>Absolutely Free to Join!</li>
        <li><svg width="12" height="12" viewBox="0 0 12 12"><path d="M1 6.5l3 3 7-7" fill="none" stroke="#fff" stroke-width="1.8"/></svg>You'll earn 1 point for every dollar you spend</li>
        <li><svg width="12" height="12" viewBox="0 0 12 12"><path d="M1 6.5l3 3 7-7" fill="none" stroke="#fff" stroke-width="1.8"/></svg>Earn double points on select items purchased</li>
        <li><svg width="12" height="12" viewBox="0 0 12 12"><path d="M1 6.5l3 3 7-7" fill="none" stroke="#fff" stroke-width="1.8"/></svg>Earn 25 points when you refer a friend</li>
      </ul>
    </section>

    <div class="thanks-band">It's Just Our Way of Saying <strong>Thank You!</strong></div>

    <div class="service-pennant">
      <svg width="205" height="200" viewBox="0 0 205 200"><polygon points="0,0 205,0 205,150 102.5,200 0,150" fill="var(--brand-red)"/></svg>
      <p class="service-text">See Our<br>Customer<br>Service<br>Representative<br>Today!</p>
    </div>

    <section class="exclusives">
      <h2 class="exclusives-title">Exclusives:</h2>
      <ul class="exclusives-list">
        <li>VIP access to our special events</li>
        <li>Be the first to know about our specials</li>
        <li>Receive notice on non-advertised specials</li>
        <li>Free subscription to our online newsletter</li>
        <li>Free gift with sign up</li>
        <li>Special “members only” shopping events</li>
      </ul>
    </section>

    <footer class="contact">
      12 Harbour Way, K.T.N. Mini Mall | P.O. Box F 51830, Port Carrow,<br>
      Coral Key, Isla Verde | Tel: (242) 555 0148/9 | Fax: (242) 555 0150<br>
      www.vitalleafpharmacy.com
    </footer>
  </main>
</body>
</html>
```